Startup company business card (Media & Advertising)

we need a business card design for a company that is a startup in the media and aggregation industry. Card needs to look funky and of a new breed/modern and upmarket.

Target Market(s)

advertisers/ brand agencies & media publishers

Industry/Entity Type

Advertising

Contact Information for Business Card

Please ensure the front face signifies our brand (plintovo.com) and back has details for the contact. Standard contact such as phone , address, email , website etc.

Font styles to use
Other font styles liked:
• use styleguide and logo font and color

Colors

Designer to choose colors to be used in the design.

Requirements
Must have
• We are disrupting the media and agency industry so subtlety would be good to use imagery to signify this
Nice to have
• Please use logo colors for branding
Should not have
• be as creative and provide few options. Pick a brand color from logo and styleguide

```html
<!DOCTYPE html>
<html lang="en">
<head>
<meta charset="utf-8">
<title>plintovo business card</title>
<link rel="stylesheet" href="https://fonts.googleapis.com/css2?family=Work+Sans:wght@400;500;700&display=swap">
<style>
  :root {
    --stage: #1f1f1f;
    --brand-red: #d9474b;
    --accent-red: #e8303f;
    --ink: #1a1a1a;
    --paper: #ffffff;
    --hole-light: #ffffff;
    --hole-shade: #d8d8d8;
  }
  * { margin: 0; padding: 0; box-sizing: border-box; }
  html, body { width: 1200px; height: 930px; overflow: hidden; }
  body {
    background: var(--stage);
    font-family: "Work Sans", sans-serif;
    position: relative;
  }
  .card {
    position: absolute;
    width: 620px;
    height: 360px;
    border-radius: 18px;
    overflow: hidden;
    box-shadow: 0 18px 40px rgba(0,0,0,0.45);
  }
  /* Front face */
  .card-front { left: 80px; top: 70px; background: var(--brand-red); }
  .torn-reveal {
    position: absolute;
    left: 170px; top: 55px;
    width: 290px; height: 250px;
    border-radius: 46% 40% 44% 38%;
    background: radial-gradient(circle at 50% 50%, var(--hole-light) 40%, #efefef 70%, var(--hole-shade) 100%);
  }
  .front-lockup {
    position: absolute;
    left: 190px; top: 140px;
    width: 250px;
    text-align: center;
  }
  .brand-name {
    display: inline-flex;
    align-items: center;
    gap: 12px;
    font-weight: 700;
    color: var(--ink);
    letter-spacing: 0.5px;
  }
  .brand-dot { display: inline-block; border-radius: 50%; background: var(--accent-red); }
  .front-lockup .brand-name { font-size: 34px; }
  .front-lockup .brand-dot { width: 26px; height: 26px; }
  .tagline {
    margin-top: 8px;
    font-size: 15px;
    font-weight: 500;
    color: var(--accent-red);
  }
  /* Back face */
  .card-back { left: 500px; top: 480px; background: var(--paper); }
  .back-lockup { position: absolute; left: 50px; top: 168px; }
  .back-lockup .brand-name { font-size: 44px; }
  .back-lockup .brand-dot { width: 38px; height: 38px; }
  .divider {
    position: absolute;
    left: 345px; top: 100px;
    width: 1.5px; height: 150px;
    background: var(--accent-red);
  }
  .contact { position: absolute; left: 365px; top: 92px; color: var(--ink); }
  .contact-name {
    font-size: 19px; font-weight: 500;
    color: var(--accent-red);
    text-transform: uppercase;
    letter-spacing: 0.3px;
  }
  .contact-role { font-size: 14px; margin: 2px 0 10px; }
  .contact-address { font-size: 13px; line-height: 1.35; margin-bottom: 10px; }
  .contact-list { list-style: none; font-size: 13px; line-height: 1.5; }
  .contact-list li { display: flex; align-items: center; gap: 8px; }
  .contact-list svg { width: 11px; height: 11px; flex: none; }
</style>
</head>
<body>
  <section class="card card-front" aria-label="Card front">
    <div class="torn-reveal" role="img" aria-label="Torn paper opening revealing white paper beneath the red surface"></div>
    <div class="front-lockup">
      <div class="brand-name"><span class="brand-dot"></span>plintovo</div>
      <p class="tagline">Advertise anywhere, anytime!</p>
    </div>
  </section>

  <section class="card card-back" aria-label="Card back">
    <div class="back-lockup">
      <div class="brand-name"><span class="brand-dot"></span>plintovo</div>
    </div>
    <div class="divider"></div>
    <div class="contact">
      <p class="contact-name">Daniel Harper</p>
      <p class="contact-role">Director</p>
      <p class="contact-address">2215 Harbor Lane<br>Riverton, WA 98120</p>
      <ul class="contact-list">
        <li>
          <svg viewBox="0 0 24 24" aria-hidden="true"><path fill="#e8303f" d="M6.6 10.8a15 15 0 0 0 6.6 6.6l2.2-2.2a1 1 0 0 1 1-.25 11.4 11.4 0 0 0 3.6.57 1 1 0 0 1 1 1V20a1 1 0 0 1-1 1A17 17 0 0 1 3 4a1 1 0 0 1 1-1h3.5a1 1 0 0 1 1 1c0 1.25.2 2.45.57 3.57a1 1 0 0 1-.25 1z"/></svg>
          +41795550187
        </li>
        <li>
          <svg viewBox="0 0 24 24" aria-hidden="true"><rect x="2" y="5" width="20" height="14" rx="2" fill="none" stroke="#e8303f" stroke-width="2.4"/><path d="M2 6l10 7 10-7" fill="none" stroke="#e8303f" stroke-width="2.4"/></svg>
          info@plintovo.com
        </li>
        <li>
          <svg viewBox="0 0 24 24" aria-hidden="true"><circle cx="12" cy="12" r="10" fill="none" stroke="#e8303f" stroke-width="2.4"/><path d="M2 12h20M12 2c3 3 3 17 0 20M12 2c-3 3-3 17 0 20" fill="none" stroke="#e8303f" stroke-width="2"/></svg>
          www.plintovo.com
        </li>
      </ul>
    </div>
  </section>
</body>
</html>
```